Bottle label design for a mulberry brandy

Please create a label design for a mulberry brandy. The registered brand name is "Kolvat"
The brandy will be produced in Armenia from 100% mulberry.
Color of the product: transparent.
The product will be sold worldwide. The price will be between 30 and 50 USD. So the product will be in premium category.
Therefore we need a solid design, appropriate to the product price category. The design, however, needs to be modern and optimistic.
You can have mulberries on the label or not have, it is up to you.
We have chosen for the product some bottle types, the links to the available bottles you can find in the attachment. Ideally you show a picture of your label on the bottle you selected.

Target Market(s)

worldwide

```html
<!DOCTYPE html>
<html lang="en">
<head>
<meta charset="utf-8">
<title>Kolvat Mulberry Brandy – Label</title>
<link rel="stylesheet" href="https://fonts.googleapis.com/css2?family=Rye&family=Oswald:wght@500;600&family=Pirata+One&family=Sacramento&family=Montserrat:wght@700&display=swap">
<style>
  :root {
    --stage: #2e2d3b;
    --paper: #eeeeef;
    --paper-shade: #dedfe1;
    --ink: #2a2937;
    --gold: #8a7440;
    --gold-dark: #6e5c33;
    --orange: #e17a45;
    --orange-deep: #b04a22;
    --rust: #9a3c1b;
  }
  html, body {
    margin: 0;
    width: 1200px;
    height: 865px;
    overflow: hidden;
    background: var(--stage);
  }
  .canvas {
    position: relative;
    width: 1200px;
    height: 865px;
  }
  .label {
    position: absolute;
    left: 340px;
    top: 22px;
    width: 520px;
    height: 820px;
    display: block;
  }
  .brand-title { font-family: "Rye", serif; font-size: 150px; }
  .brand-sub { font-family: "Oswald", sans-serif; font-weight: 600; font-size: 34px; fill: var(--gold); letter-spacing: 1px; }
  .banner-text { font-family: "Oswald", sans-serif; font-weight: 600; font-size: 24px; fill: var(--gold); }
  .badge-text { font-family: "Montserrat", sans-serif; font-weight: 700; font-size: 10.5px; fill: #ffffff; letter-spacing: 1.2px; }
  .panel-name { font-family: "Oswald", sans-serif; font-weight: 600; font-size: 30px; fill: var(--ink); }
  .panel-facts { font-family: "Pirata One", serif; font-size: 19px; fill: var(--ink); }
  .panel-script { font-family: "Sacramento", cursive; fill: var(--ink); }
  .dotted { stroke: var(--ink); stroke-width: 2; stroke-dasharray: 2 3; fill: none; }
</style>
</head>
<body>
<div class="canvas">
  <svg class="label" viewBox="0 0 520 820" xmlns="http://www.w3.org/2000/svg">
    <defs>
      <linearGradient id="title-fill" x1="0" y1="0" x2="0" y2="1">
        <stop offset="0" stop-color="#8f7a45"/>
        <stop offset="0.45" stop-color="#6a5c45"/>
        <stop offset="1" stop-color="#2c2b40"/>
      </linearGradient>
      <linearGradient id="band-fill" x1="0" y1="0" x2="1" y2="0">
        <stop offset="0" stop-color="#c45a2c"/>
        <stop offset="0.5" stop-color="#e38150"/>
        <stop offset="1" stop-color="#d06a3a"/>
      </linearGradient>
      <radialGradient id="artwork-fill" cx="0.5" cy="0.55" r="0.6">
        <stop offset="0" stop-color="#5a5a68"/>
        <stop offset="0.55" stop-color="#a9a9b1"/>
        <stop offset="1" stop-color="#e6e6e8"/>
      </radialGradient>
      <radialGradient id="badge-core" cx="0.5" cy="0.5" r="0.5">
        <stop offset="0" stop-color="#f2a070"/>
        <stop offset="1" stop-color="#b04a22"/>
      </radialGradient>
      <pattern id="zigzag" width="6" height="7" patternUnits="userSpaceOnUse">
        <polygon points="0,7 3,0 6,7" fill="#c45a2c"/>
      </pattern>
      <path id="banner-curve" d="M100,555 Q260,639 420,555"/>
      <path id="badge-top" d="M17,700 A55,55 0 0 1 127,700"/>
      <path id="badge-bottom" d="M9,700 A63,63 0 0 0 135,700"/>
    </defs>

    <!-- paper -->
    <rect class="paper" x="0" y="0" width="520" height="820" fill="var(--paper)"/>
    <rect x="0" y="0" width="520" height="14" fill="var(--orange)"/>
    <rect x="0" y="14" width="520" height="3" fill="var(--rust)"/>

    <!-- brand header -->
    <g class="brand-header">
      <text class="brand-title" x="260" y="205" text-anchor="middle" textLength="470" lengthAdjust="spacingAndGlyphs" fill="url(#title-fill)">Kolvat</text>
      <text class="brand-sub" x="490" y="250" text-anchor="end">MULBERRY BRANDY</text>
    </g>

    <!-- fruit artwork area -->
    <rect class="fruit-artwork" role="img" aria-label="Engraved ink illustration of a mulberry branch with ripe berries and leaves"
          x="38" y="265" width="456" height="245" rx="20" fill="url(#artwork-fill)"/>

    <!-- curved banner -->
    <g class="banner">
      <path d="M92,528 Q260,612 428,528" fill="none" stroke="var(--ink)" stroke-width="1.5"/>
      <path d="M92,566 Q260,650 428,566" fill="none" stroke="var(--ink)" stroke-width="1.5"/>
      <text class="banner-text" text-anchor="middle">
        <textPath href="#banner-curve" startOffset="50%">100% MULBERRY BRANDY</textPath>
      </text>
    </g>

    <!-- info band -->
    <g class="info-band">
      <rect x="0" y="615" width="520" height="7" fill="url(#zigzag)"/>
      <rect x="0" y="622" width="520" height="198" fill="url(#band-fill)"/>

      <g class="origin-badge">
        <circle cx="72" cy="700" r="68" fill="var(--ink)"/>
        <circle cx="72" cy="700" r="66" fill="none" stroke="#ffffff" stroke-width="1.5"/>
        <circle cx="72" cy="700" r="46" fill="url(#badge-core)"/>
        <rect role="img" aria-label="Map silhouette of Armenia" x="52" y="668" width="40" height="64" rx="10" fill="#1c1b22"/>
        <text class="badge-text" text-anchor="middle"><textPath href="#badge-top" startOffset="50%">PRODUCED IN ARMENIA</textPath></text>
        <text class="badge-text" text-anchor="middle"><textPath href="#badge-bottom" startOffset="50%">COUNTRY IN ASIA</textPath></text>
      </g>

      <g class="product-facts">
        <text class="panel-name" x="152" y="675" textLength="352" lengthAdjust="spacingAndGlyphs">KOLVAT MULBERRY BRANDY</text>
        <line class="dotted" x1="152" y1="690" x2="505" y2="690"/>
        <text class="panel-facts" x="152" y="724" textLength="352" lengthAdjust="spacingAndGlyphs">___ ML ___%ALC VOL ___ STANDARD DRINKS</text>
        <line class="dotted" x1="152" y1="740" x2="505" y2="740"/>
        <text class="panel-script" x="152" y="778" font-size="20">Produced in Armenia</text>
        <line class="dotted" x1="346" y1="754" x2="346" y2="794"/>
        <text class="panel-script" x="356" y="776" font-size="17">www.kolvatspirits.com</text>
      </g>
    </g>
  </svg>
</div>
</body>
</html>
```